Business Card Design Harbor of Calm

mental health provider
contemporary
warmth
inviting

Target Market(s)

mental health clients adults

Industry/Entity Type

Mental Health

Contact Information for Business Card

Danielle Arkwright PMHNP
2841 SW Tenley Ave
Suite 384C
Portland OR 97318
Fax 503-555-0182
Tel 503-555-0147
Email danielle@darkwright.example
Website darkwright.example

Requirements
Nice to have
• see above
Should not have
• no medical logos

```html
<!DOCTYPE html>
<html lang="en">
<head>
<meta charset="utf-8">
<title>Harbor of Calm – Business Card</title>
<link rel="stylesheet" href="https://fonts.googleapis.com/css2?family=Arimo:wght@400;700&family=Pinyon+Script&display=swap">
<style>
  :root {
    --stage: #2b2b2b;
    --lime: #8dc63f;
    --lime-deep: #7ab52e;
    --lime-soft: #bcd97a;
    --lime-band: rgba(255, 255, 255, 0.22);
    --cream: #faf8ef;
    --brown: #6b3a1c;
    --brown-dark: #5a2e14;
    --white: #ffffff;
  }
  * { margin: 0; padding: 0; box-sizing: border-box; }
  html, body {
    width: 1200px; height: 900px; overflow: hidden;
    background: var(--stage);
  }
  .stage {
    position: relative; width: 1200px; height: 900px;
  }
  .card {
    position: absolute; left: 250px; width: 700px; height: 400px;
    overflow: hidden;
    box-shadow: 0 6px 18px rgba(0, 0, 0, 0.45);
  }

  /* Back side */
  .card-back {
    top: 40px;
    background: linear-gradient(135deg, var(--lime) 0%, var(--lime-deep) 100%);
  }
  .card-back .band {
    position: absolute; left: 0; right: 0; top: 230px; height: 46px;
    background: var(--lime-band);
  }
  .card-back .wordmark {
    position: absolute; left: 0; right: 0; top: 120px;
    text-align: center;
    font-family: "Pinyon Script", cursive;
    font-size: 68px; color: var(--white);
    line-height: 1;
  }
  .card-back .website {
    position: absolute; left: 0; right: 0; top: 238px;
    text-align: center;
    font-family: "Arimo", sans-serif;
    font-size: 22px; letter-spacing: 6px;
    color: var(--lime-deep);
  }

  /* Front side */
  .card-front {
    top: 470px;
    background: var(--lime-soft);
  }
  .card-front .top-strip {
    position: absolute; left: 0; right: 0; top: 0; height: 26px;
    background: var(--brown);
  }
  .card-front .header {
    position: absolute; left: 0; right: 0; top: 26px; height: 176px;
    background: var(--cream);
    border-bottom: 3px solid var(--brown);
  }
  .card-front .wordmark {
    position: absolute; left: 0; right: 0; top: 52px;
    text-align: center;
    font-family: "Pinyon Script", cursive;
    font-size: 66px; color: var(--brown);
    line-height: 1;
  }
  .card-front .holder {
    position: absolute; left: 40px; top: 300px;
    font-family: "Arimo", sans-serif;
    font-size: 21px; color: var(--brown);
  }
  .holder .holder-name { font-weight: 700; }
  .card-front .divider {
    position: absolute; left: 392px; top: 206px; width: 1px; height: 150px;
    background: rgba(107, 58, 28, 0.25);
  }
  .contact-list {
    position: absolute; left: 408px; top: 218px;
    list-style: none;
    font-family: "Arimo", sans-serif;
    font-size: 16px; color: var(--brown);
    line-height: 22px;
  }
  .contact-list li {
    display: flex; align-items: flex-start; gap: 12px;
  }
  .contact-list .icon {
    width: 14px; height: 14px; margin-top: 4px; flex: none;
    fill: var(--brown-dark);
  }
  .contact-list .primary { font-weight: 700; }
</style>
</head>
<body>
<main class="stage">

  <section class="card card-back" aria-label="Business card, back">
    <div class="band"></div>
    <div class="wordmark">Danielle Arkwright</div>
    <div class="website">www.darkwright.example</div>
  </section>

  <section class="card card-front" aria-label="Business card, front">
    <div class="top-strip"></div>
    <div class="header">
      <div class="wordmark">Danielle Arkwright</div>
    </div>

    <p class="holder"><span class="holder-name">DANIELLE ARKWRIGHT</span> PMHNP</p>

    <div class="divider"></div>

    <ul class="contact-list">
      <li>
        <svg class="icon" viewBox="0 0 16 16" aria-hidden="true"><path d="M3.5 1.5l2.5 0 1.2 3.2-1.6 1.1c.8 1.8 2.3 3.3 4.1 4.1l1.1-1.6 3.2 1.2v2.5c0 .8-.7 1.5-1.5 1.5C6.4 13.5 2 9.1 2 3c0-.8.7-1.5 1.5-1.5z"/></svg>
        <span class="primary">503 555 0147</span>
      </li>
      <li>
        <svg class="icon" viewBox="0 0 16 16" aria-hidden="true"><rect x="4" y="1" width="8" height="5"/><rect x="1" y="6" width="14" height="7" rx="1.5"/><rect x="4" y="10" width="8" height="5" fill="#bcd97a"/></svg>
        <span>503 555 0182</span>
      </li>
      <li>
        <svg class="icon" viewBox="0 0 16 16" aria-hidden="true"><circle cx="8" cy="8" r="6.5" fill="none" stroke="#5a2e14" stroke-width="1.5"/><path d="M1.5 8h13M8 1.5c-3 3.5-3 9.5 0 13M8 1.5c3 3.5 3 9.5 0 13" fill="none" stroke="#5a2e14" stroke-width="1.2"/></svg>
        <span>www.darkwright.example</span>
      </li>
      <li>
        <svg class="icon" viewBox="0 0 16 16" aria-hidden="true"><rect x="1" y="3" width="14" height="10" rx="1"/><path d="M1.5 3.5L8 9l6.5-5.5" fill="none" stroke="#bcd97a" stroke-width="1.3"/></svg>
        <span>danielle@darkwright.example</span>
      </li>
      <li>
        <svg class="icon" viewBox="0 0 16 16" aria-hidden="true"><path d="M8 1a5 5 0 0 0-5 5c0 3.8 5 9 5 9s5-5.2 5-9a5 5 0 0 0-5-5zm0 7a2 2 0 1 1 0-4 2 2 0 0 1 0 4z"/></svg>
        <span>2841 SW Tenley Ave Suite 384C<br>Portland OR 97318</span>
      </li>
    </ul>
  </section>

</main>
</body>
</html>
```